Harwell Renewal
Project: Business card design
Business card design  - Emergency Services
Business card design
Bright & Fun-filled
3871 Pelton Ave Brookvale, OH 45817
harwellrenewalbrookvale@mailvista.net
I want a 24hr symbol on there I want little logos showing we do water, fire, mold, odor I want little logos for phone, email, website, location, and also one for FB. the fb is @harwellrenewalbrookvale Bright colors, similar to logo. Black, silver, blue preferred colors.
our large logo and maybe the symbols showing we do water, fire, mold, odor

```html
<!DOCTYPE html>
<html lang="en">
<head>
<meta charset="utf-8">
<title>Harwell Renewal – Business Card</title>
<link rel="stylesheet" href="https://fonts.googleapis.com/css2?family=Montserrat:wght@400;600;700;800&display=swap">
<style>
  :root {
    --stage: #2b2e33;
    --navy: #1e2430;
    --navy-deep: #161b24;
    --white: #ffffff;
    --ink: #1e2430;
    --green: #7cc242;
    --blue: #2a8fd6;
    --orange: #f08a24;
    --red: #e2412f;
    --muted: #8a93a3;
  }
  * { box-sizing: border-box; margin: 0; padding: 0; }
  html, body { width: 1200px; height: 1023px; overflow: hidden; }
  body {
    background: var(--stage);
    font-family: "Montserrat", Arial, sans-serif;
    position: relative;
  }
  .card {
    position: absolute;
    left: 160px;
    width: 880px;
    height: 470px;
    overflow: hidden;
    box-shadow: 0 10px 30px rgba(0,0,0,.45);
    background: var(--navy);
  }
  .card--front { top: 28px; }
  .card--back { top: 525px; }

  /* Brand lockup */
  .brand { position: absolute; display: flex; align-items: center; gap: 20px; }
  .brand__mark { width: 74px; height: 74px; border-radius: 12px; background: var(--blue); flex: none; }
  .brand__text { display: flex; flex-direction: column; gap: 8px; }
  .brand__name {
    font-weight: 800; font-size: 44px; letter-spacing: 1px;
    line-height: 1; text-transform: uppercase;
  }
  .brand__tagline {
    font-weight: 600; font-size: 13px; letter-spacing: 4px; text-transform: uppercase;
  }
  .card--front .brand { left: 210px; top: 100px; }
  .card--front .brand__name { color: var(--white); }
  .card--front .brand__tagline { color: var(--muted); }

  /* Service band */
  .services {
    position: absolute; left: 0; right: 0; top: 290px; height: 110px;
    background: var(--white);
    display: flex; justify-content: center; align-items: center; gap: 52px;
  }
  .service { display: flex; flex-direction: column; align-items: center; gap: 6px; }
  .service__icon {
    width: 52px; height: 52px; border: 2.5px solid var(--ink); border-radius: 50%;
    display: flex; align-items: center; justify-content: center;
  }
  .service__icon svg { width: 26px; height: 26px; }
  .service__label { font-size: 11px; font-weight: 600; letter-spacing: 1px; color: var(--ink); }

  /* Back */
  .back__topbar { position: absolute; left: 0; right: 0; top: 0; height: 28px; background: var(--navy-deep); }
  .back__light { position: absolute; left: 0; right: 0; top: 28px; height: 170px; background: var(--white); }
  .card--back .brand { left: 180px; top: 62px; }
  .card--back .brand__name { color: var(--ink); }
  .card--back .brand__tagline { color: var(--blue); }

  .contact { position: absolute; left: 160px; top: 232px; }
  .contact__name {
    color: var(--green); font-weight: 800; font-size: 28px; letter-spacing: 1px;
    text-transform: uppercase; margin-bottom: 16px;
  }
  .contact__list { list-style: none; }
  .contact__item {
    display: flex; align-items: center; gap: 12px;
    color: var(--white); font-size: 16px; margin-bottom: 10px;
  }
  .contact__icon {
    width: 22px; height: 22px; border-radius: 50%;
    display: flex; align-items: center; justify-content: center; flex: none;
  }
  .contact__icon svg { width: 12px; height: 12px; }
  .contact__icon--phone { background: var(--orange); }
  .contact__icon--mail { background: var(--red); }
  .contact__icon--pin { background: var(--orange); }
  .contact__icon--social { background: var(--blue); border-radius: 4px; }

  .badge-24 { position: absolute; right: 90px; top: 225px; width: 150px; height: 150px; }
</style>
</head>
<body>

<section class="card card--front">
  <div class="brand">
    <div class="brand__mark"></div>
    <div class="brand__text">
      <div class="brand__name">Harwell Renewal</div>
      <div class="brand__tagline">Water · Fire · Mold</div>
    </div>
  </div>
  <div class="services">
    <div class="service">
      <div class="service__icon">
        <svg viewBox="0 0 24 24"><path d="M12 2 C8 8 5 11 5 15 a7 7 0 0 0 14 0 c0-4-3-7-7-13z" fill="none" stroke="#1e2430" stroke-width="2"/></svg>
      </div>
      <span class="service__label">WATER</span>
    </div>
    <div class="service">
      <div class="service__icon">
        <svg viewBox="0 0 24 24"><path d="M12 2 c1 5 6 7 6 13 a6 6 0 0 1-12 0 c0-3 2-5 3-6 c0 3 1 4 2 4 c0-4 -1-7 1-11z" fill="none" stroke="#1e2430" stroke-width="2" stroke-linejoin="round"/></svg>
      </div>
      <span class="service__label">FIRE</span>
    </div>
    <div class="service">
      <div class="service__icon">
        <svg viewBox="0 0 24 24" fill="none" stroke="#1e2430" stroke-width="2"><circle cx="12" cy="12" r="4"/><circle cx="5" cy="6" r="2"/><circle cx="19" cy="7" r="2"/><circle cx="6" cy="19" r="2"/><circle cx="18" cy="18" r="2"/></svg>
      </div>
      <span class="service__label">MOLD</span>
    </div>
    <div class="service">
      <div class="service__icon">
        <svg viewBox="0 0 24 24" fill="none" stroke="#1e2430" stroke-width="2" stroke-linecap="round"><path d="M7 20 c-3-4 3-6 0-10 s3-6 0-8"/><path d="M12 20 c-3-4 3-6 0-10 s3-6 0-8"/><path d="M17 20 c-3-4 3-6 0-10 s3-6 0-8"/></svg>
      </div>
      <span class="service__label">ODOR</span>
    </div>
  </div>
</section>

<section class="card card--back">
  <div class="back__topbar"></div>
  <div class="back__light"></div>
  <div class="brand">
    <div class="brand__mark"></div>
    <div class="brand__text">
      <div class="brand__name">Harwell Renewal</div>
      <div class="brand__tagline">Water · Fire · Mold</div>
    </div>
  </div>

  <div class="contact">
    <h2 class="contact__name">Harwell Renewal</h2>
    <ul class="contact__list">
      <li class="contact__item">
        <span class="contact__icon contact__icon--phone"><svg viewBox="0 0 24 24"><path d="M5 3h4l2 5-3 2a12 12 0 0 0 6 6l2-3 5 2v4a2 2 0 0 1-2 2A18 18 0 0 1 3 5a2 2 0 0 1 2-2z" fill="#fff"/></svg></span>
        555.210.0142
      </li>
      <li class="contact__item">
        <span class="contact__icon contact__icon--mail"><svg viewBox="0 0 24 24" fill="none" stroke="#fff" stroke-width="2.5"><rect x="3" y="5" width="18" height="14"/><path d="M3 6l9 7 9-7"/></svg></span>
        harwellrenewalbrookvale@mailvista.net
      </li>
      <li class="contact__item">
        <span class="contact__icon contact__icon--pin"><svg viewBox="0 0 24 24"><path d="M12 2a7 7 0 0 0-7 7c0 5 7 13 7 13s7-8 7-13a7 7 0 0 0-7-7z" fill="#fff"/><circle cx="12" cy="9" r="2.5" fill="#f08a24"/></svg></span>
        3871 Pelton Ave Brookvale, OH 45817
      </li>
      <li class="contact__item">
        <span class="contact__icon contact__icon--social"></span>
        @harwellrenewalbrookvale
      </li>
    </ul>
  </div>

  <svg class="badge-24" viewBox="0 0 150 150" role="img" aria-label="24 hour service">
    <circle cx="75" cy="75" r="66" fill="none" stroke="var(--blue)" stroke-width="8"/>
    <path d="M30 38 A58 58 0 0 1 120 38" fill="none" stroke="var(--green)" stroke-width="8" stroke-linecap="round"/>
    <circle cx="75" cy="75" r="54" fill="#12171f"/>
    <text x="75" y="82" text-anchor="middle" font-family="Montserrat, Arial, sans-serif" font-weight="800" font-size="44" fill="var(--green)">24</text>
    <text x="75" y="106" text-anchor="middle" font-family="Montserrat, Arial, sans-serif" font-weight="700" font-size="15" letter-spacing="2" fill="#ffffff">HOUR</text>
  </svg>
</section>

</body>
</html>
```